Gift Voucher For Medical Cosmetic Clinic

I need a high end, beautiful gift voucher for my Cosmetic Medical Clinic that I will provide to customers in a beautifully designed envelope. I like the colours blue with different tones of blue, white and silver. I have attached my business card for further information.
The address is: 4/15 Kelbrook Lane, Tollbrook, Christchurch 8041.
Phone: 0800-547-391
Email: lorel@vumeko.co.nz
Website: www.vumeko.co.nz

```html
<!DOCTYPE html>
<html lang="en">
<head>
<meta charset="utf-8">
<title>Vumeko Gift Voucher</title>
<link href="https://fonts.googleapis.com/css2?family=Cinzel:wght@400&family=Kalam:wght@300&family=Montserrat:wght@500&family=Roboto:wght@300;400&display=swap" rel="stylesheet">
<style>
  :root{
    --stage:#e6e6e6;
    --blue-deep:#0a63b0;
    --blue-mid:#2a8ad6;
    --blue-light:#55b6ec;
    --white:#ffffff;
    --silver-dark:#a9acaf;
    --silver-light:#f7f7f7;
    --ink:#1c1c1c;
  }
  html,body{margin:0;padding:0;overflow:hidden}
  body{width:1200px;height:940px;background:var(--stage);position:relative;font-family:'Roboto',sans-serif;color:var(--white)}
  .card{position:absolute;left:239px;width:722px;height:323px;overflow:hidden;
    background:linear-gradient(115deg,var(--blue-deep) 0%,var(--blue-mid) 55%,var(--blue-light) 100%)}
  .voucher{top:133px}
  .back{top:484px}
  .center{position:absolute;text-align:center;white-space:nowrap}
  .brand-dot{position:absolute;border-radius:50%;border:2px solid var(--silver-light);box-sizing:border-box}
  .brand-name{position:absolute;font-family:'Cinzel',serif;font-weight:400;color:var(--silver-light);letter-spacing:2px;line-height:1;white-space:nowrap}
  .brand-tag{position:absolute;font-family:'Cinzel',serif;color:var(--white);letter-spacing:1px;line-height:1;white-space:nowrap}
  .silver-band{position:absolute;left:0;
    background:linear-gradient(90deg,var(--silver-dark) 0%,var(--silver-light) 35%,var(--silver-light) 60%,var(--silver-dark) 100%);
    color:var(--ink);font-family:'Montserrat',sans-serif;font-weight:500;font-size:13px;letter-spacing:.4px;
    display:flex;align-items:center;justify-content:center}
  /* voucher front */
  .voucher .brand-dot{left:80px;top:27px;width:68px;height:68px}
  .voucher .brand-name{left:172px;top:34px;font-size:38px}
  .voucher .brand-tag{left:174px;top:74px;font-size:15px}
  .program{left:0;width:414px;top:116px;font-size:16px;font-weight:300}
  .title{left:0;width:414px;top:140px;font-family:'Cinzel',serif;font-size:42px;letter-spacing:1px;line-height:44px}
  .special{left:0;width:414px;top:181px;font-family:'Kalam',cursive;font-weight:300;font-size:15px;letter-spacing:1px;line-height:20px}
  .thanks{left:0;width:414px;top:209px;font-size:16px;font-weight:300}
  .voucher .silver-band{top:246px;width:470px;height:26px}
  .follow{left:0;width:414px;top:282px;font-size:14px}
  .photo{position:absolute;left:400px;top:0;width:322px;height:323px}
  .badge{position:absolute;left:391px;top:117px;width:108px;height:108px}
  .badge-text{position:absolute;left:391px;top:141px;width:108px;text-align:center}
  .badge-label{font-size:7px;letter-spacing:3px;display:block}
  .badge-value{font-size:44px;font-weight:400;line-height:1;letter-spacing:-1px}
  /* back */
  .back .brand-dot{left:168px;top:32px;width:108px;height:108px}
  .back .brand-name{left:300px;top:40px;font-size:58px;letter-spacing:3px}
  .back .brand-tag{left:302px;top:106px;font-size:24px}
  .services{left:0;width:722px;top:170px;font-size:16px}
  .contact{left:0;width:722px;top:217px;font-size:16px;display:flex;justify-content:center;gap:20px;align-items:center}
  .contact span{display:inline-flex;align-items:center;gap:8px}
  .address{left:0;width:722px;top:240px;font-size:16px}
  .back .silver-band{top:288px;width:722px;height:35px}
</style>
</head>
<body>

<section class="card voucher">
  <div class="brand-dot"></div>
  <div class="brand-name">VUMEKO</div>
  <div class="brand-tag">AESTHETIC DOCTOR</div>
  <div class="center program">Customer Appreciation program</div>
  <div class="center title">Gift Voucher</div>
  <div class="center special">Special For You</div>
  <div class="center thanks">Thank you for all your support</div>
  <div class="silver-band">HOME AND SPA BASED TREATMENTS</div>
  <div class="center follow">Follow us on: &nbsp;/vumeko &nbsp;&nbsp;www.vumeko.co.nz</div>

  <svg class="photo" viewBox="0 0 322 323">
    <defs>
      <linearGradient id="photoTone" x1="0" y1="0" x2="1" y2="1">
        <stop offset="0" stop-color="#e9ecef"/>
        <stop offset=".5" stop-color="#e8c9b0"/>
        <stop offset="1" stop-color="#f4f1ee"/>
      </linearGradient>
      <linearGradient id="silverCurve" x1="0" y1="0" x2="0" y2="1">
        <stop offset="0" stop-color="#f7f7f7"/>
        <stop offset=".5" stop-color="#a9acaf"/>
        <stop offset="1" stop-color="#f7f7f7"/>
      </linearGradient>
    </defs>
    <path role="img" aria-label="Photo of a woman with a towel on her hair using a facial roller" d="M44,0 C14,80 14,180 74,240 C96,268 80,300 64,323 L322,323 L322,0 Z" fill="url(#photoTone)"/>
    <path d="M44,0 C14,80 14,180 74,240 C96,268 80,300 64,323" fill="none" stroke="url(#silverCurve)" stroke-width="5"/>
    <path d="M30,0 C0,80 2,180 60,240 C82,266 62,300 40,323" fill="none" stroke="url(#silverCurve)" stroke-width="2"/>
  </svg>

  <svg class="badge" viewBox="-54 -54 108 108">
    <polygon fill="#cfe3f2" points="0,-54 7,-44 19,-50 21,-38 34,-40 31,-28 44,-25 37,-15 48,-7 38,2 46,13 34,18 38,31 25,32 24,45 13,40 5,52 -3,42 -14,50 -18,38 -31,42 -29,29 -43,27 -36,16 -48,8 -38,0 -47,-11 -35,-16 -40,-29 -27,-29 -27,-42 -15,-37 -9,-50"/>
    <circle r="38" fill="#1479c9"/>
  </svg>
  <div class="badge-text">
    <span class="badge-label">VALUE</span>
    <span class="badge-value">$50</span>
  </div>
</section>

<section class="card back">
  <div class="brand-dot"></div>
  <div class="brand-name">VUMEKO</div>
  <div class="brand-tag">AESTHETIC DOCTOR</div>
  <div class="center services">Dermal Injectables &nbsp;| &nbsp;Plasma Facials &nbsp;| &nbsp;Microneedling &nbsp;| Skin Boosters &nbsp;| &nbsp;Excessive Sweating</div>
  <div class="center contact">
    <span>
      <svg width="14" height="14" viewBox="0 0 24 24"><path fill="#fff" d="M6.6 10.8a15 15 0 0 0 6.6 6.6l2.2-2.2c.3-.3.7-.4 1-.2 1.1.4 2.3.6 3.6.6.6 0 1 .4 1 1V20c0 .6-.4 1-1 1A17 17 0 0 1 3 4c0-.6.4-1 1-1h3.5c.6 0 1 .4 1 1 0 1.3.2 2.5.6 3.6.1.3 0 .7-.2 1z"/></svg>
      0800-547-391</span>
    <span>
      <svg width="14" height="10" viewBox="0 0 14 10"><rect x=".5" y=".5" width="13" height="9" fill="none" stroke="#fff"/><path d="M.5 .5 7 6 13.5 .5" fill="none" stroke="#fff"/></svg>
      lorel@vumeko.co.nz</span>
    <span>
      <svg width="14" height="14" viewBox="0 0 14 14"><circle cx="7" cy="7" r="6" fill="none" stroke="#fff"/><ellipse cx="7" cy="7" rx="2.6" ry="6" fill="none" stroke="#fff"/><path d="M1 7h12" stroke="#fff"/></svg>
      www.vumeko.co.nz</span>
  </div>
  <div class="center address">4/15 Kelbrook Lane, Tollbrook, Christchurch 8041</div>
  <div class="silver-band">HOME AND SPA BASED TREATMENTS</div>
</section>

</body>
</html>
```